Roofing Company Sales Rep Business Card

Business card for sales rep to canvass and hand out to property owners/managers for free roof inspections and roof replacements.

```html
<!DOCTYPE html>
<html lang="en">
<head>
<meta charset="UTF-8">
<title>Summit Crest Roofing – Business Card</title>
<link href="https://fonts.googleapis.com/css2?family=Montserrat:wght@400;500;800&display=swap" rel="stylesheet">
<style>
  :root {
    --page-bg: #121212;
    --card-top: #2c2c2c;
    --card-bottom: #1e1e1e;
    --brand-red: #e3262c;
    --text-light: #f2f2f2;
    --emboss-grey: #6b6b6b;
  }
  * { margin: 0; padding: 0; box-sizing: border-box; }
  html, body {
    width: 1200px; height: 900px; overflow: hidden;
    background: var(--page-bg);
    font-family: "Montserrat", sans-serif;
  }
  .canvas {
    width: 1200px; height: 900px;
    display: flex; flex-direction: column;
    align-items: center; justify-content: center; gap: 40px;
  }
  .card {
    width: 680px; height: 389px;
    background: linear-gradient(135deg, var(--card-bottom), var(--card-top));
    box-shadow: 0 18px 40px rgba(0,0,0,0.6);
    position: relative;
  }
  /* Front: brand name only */
  .card-front { display: flex; align-items: center; justify-content: center; }
  .brand-emboss {
    font-weight: 800; font-size: 44px; letter-spacing: 1px;
    color: var(--emboss-grey); text-transform: uppercase;
  }
  /* Back: brand + contact details */
  .card-back { display: flex; align-items: center; padding: 0 40px 0 46px; }
  .brand-block {
    width: 250px; display: flex; align-items: center; gap: 10px;
  }
  .brand-square { width: 14px; height: 14px; background: var(--brand-red); flex: none; }
  .brand-name {
    font-weight: 800; font-size: 25px; line-height: 1.1;
    color: var(--text-light); text-transform: uppercase;
  }
  .divider {
    width: 2px; height: 200px; background: var(--brand-red);
    margin: 0 28px 0 20px; flex: none;
  }
  .contact { color: var(--text-light); }
  .person-name {
    font-weight: 800; font-size: 27px; color: var(--brand-red);
    letter-spacing: 1.5px; text-transform: uppercase;
  }
  .person-role {
    font-weight: 500; font-size: 14px; letter-spacing: 1.5px;
    text-transform: uppercase; margin-bottom: 12px;
  }
  .address { font-size: 14px; line-height: 1.45; margin-bottom: 12px; }
  .contact-list { list-style: none; font-size: 14px; line-height: 1.75; }
  .contact-list li { display: flex; align-items: center; gap: 10px; }
  .contact-icon { width: 15px; height: 15px; flex: none; }
</style>
</head>
<body>
<main class="canvas">
  <section class="card card-front" aria-label="Business card front">
    <span class="brand-emboss">Summit Crest Roofing</span>
  </section>

  <section class="card card-back" aria-label="Business card back">
    <div class="brand-block">
      <span class="brand-square"></span>
      <span class="brand-name">Summit Crest<br>Roofing</span>
    </div>
    <div class="divider"></div>
    <div class="contact">
      <h1 class="person-name">Daniel Reyes</h1>
      <p class="person-role">Manager</p>
      <p class="address">218 Ridgeview Avenue, Suite 4<br>Lakewood, CO 80215</p>
      <ul class="contact-list">
        <li>
          <svg class="contact-icon" viewBox="0 0 24 24" fill="var(--brand-red)"><path d="M6.6 10.8a15 15 0 0 0 6.6 6.6l2.2-2.2a1 1 0 0 1 1-.25 11.4 11.4 0 0 0 3.6.57 1 1 0 0 1 1 1V20a1 1 0 0 1-1 1A17 17 0 0 1 3 4a1 1 0 0 1 1-1h3.5a1 1 0 0 1 1 1c0 1.25.2 2.45.57 3.57a1 1 0 0 1-.25 1z"/></svg>
          (555) 014-2290
        </li>
        <li>
          <svg class="contact-icon" viewBox="0 0 24 24" fill="var(--brand-red)"><path d="M2 5h20v14H2z M2 5l10 7 10-7" stroke="#1e1e1e" stroke-width="1.5"/></svg>
          hello@summitcrestroofing.com
        </li>
        <li>
          <svg class="contact-icon" viewBox="0 0 24 24" fill="none" stroke="var(--brand-red)" stroke-width="2"><circle cx="12" cy="12" r="10"/><path d="M2 12h20M12 2c3 3 3 17 0 20M12 2c-3 3-3 17 0 20"/></svg>
          www.summitcrestroofing.com
        </li>
      </ul>
    </div>
  </section>
</main>
</body>
</html>
```